Business Card Design Project

I am opening my own real estate company.

Tarrow & Co. Real Estate Inc.

See attachments for ideas and colors…..
Updates

Project Deadline Extended
Reason: I paid for 5 separate items (graphic design, logo, stationery, brochure & website) all at one time. I thought they all launched at the same time but they did not. That is the reason I have to extend the date.

Target Market(s)

High end real estate properties.

Industry/Entity Type

Real Estate

Font styles to use
Serif
Decorative
Script

Requirements
Must have
• High end design. I want to appeal to very expensive properties.

```html
<!DOCTYPE html>
<html lang="en">
<head>
<meta charset="utf-8">
<title>Tarrow &amp; Co. Real Estate Inc. — Business Card</title>
<link href="https://fonts.googleapis.com/css2?family=Cinzel:wght@400;600&family=Cormorant+Garamond:wght@400;500&display=swap" rel="stylesheet">
<style>
  :root {
    --page-bg: #ffffff;
    --card-black: #0b0b0b;
    --card-edge: #161616;
    --card-glow: #262626;
    --gold-light: #e9cf7a;
    --gold: #c9a646;
    --gold-deep: #8a6a22;
    --silver: #d9d9d9;
    --grey: #a6a6a6;
    --grey-dim: #8a8a8a;
  }
  * { margin: 0; padding: 0; box-sizing: border-box; }
  html, body {
    width: 1200px;
    height: 900px;
    overflow: hidden;
    background: var(--page-bg);
  }
  .canvas {
    position: relative;
    width: 1200px;
    height: 900px;
    background: var(--page-bg);
  }
  .card {
    position: absolute;
    top: 295px;
    width: 530px;
    height: 310px;
    border-radius: 24px;
    overflow: hidden;
    background: radial-gradient(ellipse at 50% 50%, var(--card-glow) 0%, var(--card-edge) 55%, var(--card-black) 100%);
    box-shadow: 0 18px 30px rgba(0, 0, 0, 0.18);
  }
  .card--front { left: 40px; }
  .card--back { left: 630px; }

  .damask-field {
    position: absolute;
    inset: 0;
    background: radial-gradient(ellipse at 50% 45%, #2a2a2a 0%, #171717 50%, #0c0c0c 100%);
  }

  .emblem {
    position: absolute;
    left: 50%;
    top: 50%;
    transform: translate(-50%, -50%);
    display: flex;
    flex-direction: column;
    align-items: center;
  }
  .flourish {
    width: 170px;
    height: 52px;
    border-radius: 26px;
    background: radial-gradient(ellipse at 50% 50%, rgba(201, 166, 70, 0.55) 0%, rgba(138, 106, 34, 0.25) 60%, rgba(138, 106, 34, 0) 100%);
  }
  .wordmark {
    font-family: "Cinzel", serif;
    font-weight: 400;
    color: var(--gold);
    text-align: center;
    line-height: 1;
    margin: 10px 0;
  }
  .wordmark__name {
    display: block;
    font-size: 40px;
    letter-spacing: 0.5px;
  }
  .wordmark__line {
    display: block;
    font-size: 13px;
    letter-spacing: 6px;
    margin-top: 8px;
  }

  .contact {
    position: absolute;
    left: 0;
    right: 0;
    top: 92px;
    text-align: center;
  }
  .contact__name {
    font-family: "Cinzel", serif;
    font-weight: 600;
    font-size: 26px;
    letter-spacing: 1px;
    color: var(--gold);
  }
  .contact__role {
    font-family: "Cormorant Garamond", serif;
    font-size: 11px;
    color: var(--grey);
    margin-top: 2px;
  }
  .contact__phone {
    font-family: "Cormorant Garamond", serif;
    font-weight: 500;
    font-size: 27px;
    color: var(--silver);
    margin-top: 34px;
    letter-spacing: 0.5px;
  }
  .contact__line {
    font-family: "Cormorant Garamond", serif;
    font-size: 14px;
    color: var(--grey);
    letter-spacing: 0.6px;
    line-height: 1.15;
  }
</style>
</head>
<body>
<main class="canvas">
  <section class="card card--front" aria-label="Card front">
    <div class="damask-field" role="img" aria-label="Dark tone-on-tone damask pattern"></div>
    <div class="emblem">
      <div class="flourish" role="img" aria-label="Gold ornamental flourish"></div>
      <h1 class="wordmark">
        <span class="wordmark__name">TARROW &amp; CO.</span>
        <span class="wordmark__line">REAL ESTATE INC.</span>
      </h1>
      <div class="flourish" role="img" aria-label="Gold ornamental flourish"></div>
    </div>
  </section>

  <section class="card card--back" aria-label="Card back">
    <div class="contact">
      <h2 class="contact__name">MILES HARLAN</h2>
      <p class="contact__role">Manager</p>
      <p class="contact__phone">154 2290 318</p>
      <p class="contact__line">info@tarrowandcorealestateinc.com</p>
      <p class="contact__line">www.tarrowandcorealestateinc.com</p>
    </div>
  </section>
</main>
</body>
</html>
```